A Pro Immigration Film to educate undocumented workers what to do if arrested.

Oscar Nominee Tomasz Velunde (Harbor Sentinel) wrapped production on the film, MERIDIAN; WE STAY which will be distributed for the purpose of educating undocumented immigrants on what to do if arrested and detained by Bureau of Transit Oversight (BTO). The Los Angeles based Alliance for Newcomer Dignity Fund (ANDEF) is the executive producer of the video which started production on the same day President Halvorsen signed an Executive Order to deny entrance to anyone from the seven countries of Iraq, Syria, Libya, Iran, Yemen, Sudan and Somalia.

Target Market(s)

Undocumented immigrants in the USA

Industry/Entity Type

Film Production

Font styles to use
Sans Serif

Colors
3176b5
85acd3
ec1f27
f04a50
f59296

Requirements
Must have
• BILLING BLOCK:
• The Alliance for Newcomer Dignity Fund presents
• meridian; we stay (all lower case)
• Tomasz Velunde
• Marco Ferrel
• Greta Voss
• Executive Producer Rosalind Pemberly
• Produced by Howard Brekkeman Zuri Malbeck
• Written and Directed by Zuri Malbeck
• LOGO AT BOTTOM: ANDEF Logo attached
Nice to have
• The image of the prisoner looking out the window
Should not have
• Police car

```html
<!DOCTYPE html>
<html lang="en">
<head>
<meta charset="utf-8">
<title>meridian; we stay — film poster</title>
<link rel="stylesheet" href="https://fonts.googleapis.com/css2?family=Montserrat:wght@700;800&family=Roboto+Condensed:wght@700&display=swap">
<style>
  :root {
    --white: #ffffff;
    --ink: #111111;
    --mesh-dark: #3b3438;
    --mesh-mid: #5a4a4c;
    --skin-warm: #8a5a48;
    --skin-light: #b07a62;
    --jumpsuit: #b8352c;
    --jumpsuit-deep: #7e2620;
    --window-light: #cdbcb3;
    --window-shadow: #6e4a44;
    --flag-blue: #4e5f7e;
    --flag-red: #a8514f;
    --flag-grey: #b9b4b6;
  }
  * { margin: 0; padding: 0; box-sizing: border-box; }
  html, body { width: 776px; height: 1200px; overflow: hidden; background: var(--white); }
  .poster { position: relative; width: 776px; height: 1200px; overflow: hidden; font-family: "Roboto Condensed", "Arial Narrow", sans-serif; font-weight: 700; color: var(--white); }

  .key-art { position: absolute; left: 0; top: 0; width: 776px; height: 930px; display: block; }

  .presenter { position: absolute; top: 30px; left: 0; width: 100%; text-align: center; text-shadow: 0 1px 3px rgba(0,0,0,0.35); }
  .presenter-name { font-size: 31px; line-height: 36px; letter-spacing: 0; }
  .presenter-verb { font-size: 13px; line-height: 16px; }

  .title {
    position: absolute; left: 104px; top: 548px;
    font-family: "Montserrat", "Helvetica Neue", sans-serif; font-weight: 800;
    font-size: 100px; line-height: 112px; letter-spacing: -1px; text-transform: lowercase;
  }
  .title-line { display: block; }
  .title-line + .title-line { padding-left: 14px; }

  .flag-band {
    position: absolute; left: 0; top: 930px; width: 776px; height: 270px;
    background:
      linear-gradient(90deg, var(--flag-blue) 0 305px, transparent 305px),
      repeating-linear-gradient(180deg, var(--flag-red) 0 21px, var(--flag-grey) 21px 42px);
  }
  .flag-band::after {
    content: ""; position: absolute; inset: 0;
    background: linear-gradient(180deg, rgba(58,72,102,0.25), rgba(30,30,40,0.15));
  }

  .cast { position: absolute; top: 955px; left: 0; width: 100%; }
  .cast-name { position: absolute; font-size: 21px; line-height: 32px; text-align: center; }
  .cast-name span { display: block; }
  .cast-lead { left: 135px; width: 150px; }
  .cast-second { left: 333px; width: 150px; }
  .cast-third { left: 500px; width: 150px; }

  .credits { position: absolute; left: 60px; top: 1054px; font-size: 15px; line-height: 25px; }

  .client-mark {
    position: absolute; left: 550px; top: 1028px; width: 166px; height: 140px;
    background: var(--white); border: 3px solid var(--ink);
    display: flex; align-items: center; justify-content: center;
  }
  .client-name { font-size: 36px; color: var(--ink); letter-spacing: 1px; }
</style>
</head>
<body>
<div class="poster">
  <svg class="key-art" viewBox="0 0 776 930" role="img" aria-label="Photograph of a detained man in an orange jumpsuit, seen in profile, looking out through a mesh-covered window toward daylight">
    <defs>
      <filter id="soften" x="-20%" y="-20%" width="140%" height="140%"><feGaussianBlur stdDeviation="22"/></filter>
      <filter id="soften-wide" x="-30%" y="-30%" width="160%" height="160%"><feGaussianBlur stdDeviation="40"/></filter>
      <linearGradient id="base-tone" x1="0" y1="0" x2="0" y2="1">
        <stop offset="0" stop-color="#4a3e42"/>
        <stop offset="0.55" stop-color="#3d3236"/>
        <stop offset="1" stop-color="#4a302c"/>
      </linearGradient>
      <linearGradient id="window-tone" x1="0" y1="0" x2="1" y2="0">
        <stop offset="0" stop-color="#a88c82"/>
        <stop offset="0.35" stop-color="#d6c6bd"/>
        <stop offset="1" stop-color="#b39a90"/>
      </linearGradient>
      <linearGradient id="figure-tone" x1="0" y1="0" x2="0" y2="1">
        <stop offset="0" stop-color="#5a3e38"/>
        <stop offset="0.4" stop-color="#9a6450"/>
        <stop offset="1" stop-color="#6a3a30"/>
      </linearGradient>
      <linearGradient id="jumpsuit-tone" x1="0" y1="0" x2="1" y2="1">
        <stop offset="0" stop-color="#c8402f"/>
        <stop offset="1" stop-color="#7e2620"/>
      </linearGradient>
    </defs>
    <rect width="776" height="930" fill="url(#base-tone)"/>
    <rect x="0" y="0" width="440" height="930" fill="#4f4448" opacity="0.6" filter="url(#soften-wide)"/>
    <rect x="540" y="-40" width="150" height="1010" fill="url(#window-tone)" filter="url(#soften)"/>
    <rect x="690" y="-40" width="120" height="1010" fill="#6b4a44" filter="url(#soften)"/>
    <path d="M430 60 C520 80 580 200 585 330 C590 460 560 560 540 700 L540 930 L400 930 L410 500 C400 330 400 160 430 60 Z" fill="url(#figure-tone)" filter="url(#soften)"/>
    <path d="M0 400 C120 380 250 420 330 520 C400 620 420 780 430 930 L0 930 Z" fill="url(#jumpsuit-tone)" filter="url(#soften)" opacity="0.9"/>
    <rect x="0" y="0" width="776" height="930" fill="#1c1416" opacity="0.12"/>
  </svg>

  <header class="presenter">
    <p class="presenter-name">The Alliance for Newcomer Dignity Fund</p>
    <p class="presenter-verb">presents</p>
  </header>

  <h1 class="title">
    <span class="title-line">meridian;</span>
    <span class="title-line">we stay</span>
  </h1>

  <div class="flag-band" role="img" aria-label="Weathered American flag background"></div>

  <section class="cast">
    <p class="cast-name cast-lead"><span>Tomasz</span><span>Velunde</span></p>
    <p class="cast-name cast-second"><span>Marco</span><span>Ferrel</span></p>
    <p class="cast-name cast-third"><span>Greta</span><span>Voss</span></p>
  </section>

  <section class="credits">
    <p>Executive Producer Rosalind Pemberly</p>
    <p>Produced by Howard Brekkeman Zuri Malbeck</p>
    <p>Written and Directed by Zuri Malbeck</p>
  </section>

  <div class="client-mark">
    <span class="client-name">ANDEF</span>
  </div>
</div>
</body>
</html>
```